Retail korea clothing store needs a logo desgin

Retail clothing store. Our main customer is 28-35 years women. our store is located at japan town San Francisco. our theme color are black , White and sliver color. we would like modern.

Clothing

```html
<!DOCTYPE html>
<html lang="en">
<head>
<meta charset="utf-8">
<title>NARI Korean Clothing – Business Card</title>
<link href="https://fonts.googleapis.com/css2?family=Raleway:ital,wght@0,200;0,300;1,200;1,300&display=swap" rel="stylesheet">
<style>
  :root {
    --paper: #ffffff;
    --ink: #000000;
    --taupe: #6e6868;
    --pearl: #e8e8e8;
    --silver-dark: #7c7c7c;
    --silver-light: #d2d2d2;
    --panel-dark: #565656;
    --panel-light: #8c8c8c;
    --tagline: #7a7a7a;
    --label: #ffffff;
  }
  html, body {
    margin: 0;
    padding: 0;
    overflow: hidden;
    background: var(--paper);
  }
  .canvas {
    position: relative;
    width: 1200px;
    height: 1200px;
    background: var(--paper);
    overflow: hidden;
    font-family: "Raleway", sans-serif;
  }
  .card-front {
    position: absolute;
    left: 156px;
    top: 32px;
    width: 924px;
    height: 543px;
    background: var(--ink);
    border-bottom-right-radius: 136px 136px;
  }
  .card-front .brand {
    position: absolute;
    left: 0;
    width: 100%;
    top: 222px;
    margin: 0;
    text-align: center;
    padding-left: 10px;
    box-sizing: border-box;
    color: var(--paper);
    font-weight: 200;
    font-size: 84px;
    line-height: 1;
    letter-spacing: -2px;
  }
  .card-front .tagline {
    position: absolute;
    left: 0;
    width: 100%;
    top: 372px;
    margin: 0;
    padding-left: 20px;
    box-sizing: border-box;
    text-align: center;
    color: var(--tagline);
    font-style: italic;
    font-weight: 300;
    font-size: 32px;
    letter-spacing: -1px;
  }
  .card-back {
    position: absolute;
    left: 154px;
    top: 613px;
    width: 922px;
    height: 543px;
  }
  .back-brand { font-family: "Raleway", sans-serif; font-weight: 200; font-size: 88px; fill: var(--ink); letter-spacing: -3px; }
  .field-label { font-family: "Raleway", sans-serif; font-style: italic; font-weight: 300; font-size: 36px; fill: var(--label); letter-spacing: -1.5px; }
  .website-label { font-family: "Raleway", sans-serif; font-style: italic; font-weight: 300; font-size: 30px; fill: var(--ink); letter-spacing: -1.5px; }
  .back-tagline { font-family: "Raleway", sans-serif; font-style: italic; font-weight: 300; font-size: 34px; fill: #5a5a5a; letter-spacing: -1.5px; }
</style>
</head>
<body>
<div class="canvas">
  <section class="card-front">
    <h1 class="brand">NARI</h1>
    <p class="tagline">Korean Clothing.</p>
  </section>

  <svg class="card-back" viewBox="181 722 1087 640" xmlns="http://www.w3.org/2000/svg">
    <defs>
      <linearGradient id="silver-sheet" x1="0" y1="0" x2="1" y2="0.2">
        <stop offset="0" stop-color="var(--silver-dark)"/>
        <stop offset="1" stop-color="var(--silver-light)"/>
      </linearGradient>
      <linearGradient id="info-panel" x1="0" y1="0.3" x2="1" y2="0">
        <stop offset="0" stop-color="var(--panel-dark)"/>
        <stop offset="1" stop-color="var(--panel-light)"/>
      </linearGradient>
      <clipPath id="card-outline">
        <path d="M181,722 H1268 V1200 Q1268,1362 1110,1362 H181 Z"/>
      </clipPath>
    </defs>
    <g clip-path="url(#card-outline)">
      <rect class="base-layer" x="181" y="722" width="1087" height="640" fill="var(--ink)"/>
      <path class="taupe-sheet" fill="var(--taupe)"
            d="M1268,724 V1362 H185 C195,1200 200,950 232,862 C258,792 330,780 420,770 C700,745 1000,735 1268,724 Z"/>
      <path class="pearl-sheet" fill="var(--pearl)"
            d="M1268,727 V1362 H196 C208,1200 214,985 248,885 C276,815 355,796 445,788 C750,765 1050,745 1268,727 Z"/>
      <path class="silver-sheet" fill="url(#silver-sheet)"
            d="M1268,726 V1200 Q1268,1362 1110,1362 H206 C222,1200 228,995 264,898 C294,830 370,800 452,790 C800,765 1100,740 1268,726 Z"/>
      <path class="info-panel" fill="url(#info-panel)"
            d="M312,867 H1250 V1215 Q1250,1345 1110,1345 H222 C232,1200 240,1000 270,912 C281,882 296,867 312,867 Z"/>
    </g>

    <text class="back-brand" x="1232" y="837" text-anchor="end">NARI</text>

    <text class="field-label" x="328" y="940">Phone:</text>
    <text class="field-label" x="793" y="940">Fax:</text>
    <text class="field-label" x="328" y="1040">Mobile:</text>
    <text class="field-label" x="797" y="1040">Email:</text>
    <text class="field-label" x="328" y="1140">Address:</text>

    <text class="website-label" x="232" y="1334">Website:</text>
    <text class="back-tagline" x="890" y="1333">Korean Clothing.</text>
  </svg>
</div>
</body>
</html>
```